ONE PAGE WEB DESIGN NEEDED for Finance Company

We need a web design (ONE PAGE DESIGN ONLY) for a new finance website called Brightwell Lending. Brightwell Lending helps customers get the right loan, whether its a home loan, investment loan, business loan etc.

You are required to come up with just the homepage design. Professionalism and quality is the key factors in the successful design.

Here are a few design questions to help you out:

-
What information should be used on the page?
Ive provided a document which outlines all the information needed to put on homepage (attached to the brief - called brightwell_page_info). Also see the Must Have section below on this brief.

-
What links should appear in the navigation/footer?:
The navigation should provide links to the following pages (NOTE: services link has subcategories):
1 Homepage
2 Services
- Home loans
- Investment loans
- Refinancing loans
- Business loans
3 About Us
4 FAQ
5 Contact Us

-
What colors should be used in the design?
Our company colors - Cyan: #2EADE3, Blue: #004B70, White. Feel free to submit designs with slight variations if you feel it improves the design.

-
What should the layout of the page be?
This is up to you to come up with - we are open to different layouts for the page design (as long as they capture the information effectively and making it easy to understand).

Target Market(s)

Potential Home owners, Families and Business Owners

Industry/Entity Type

Business

Requirements
Must have
• - Must contain our logo (attached as PNG and Illustrator file)
- Winning designer must supply a Photoshop file (PSD) that will allow us.
Nice to have
• - Should include photos/images of families, professional groups, tradespeople etc (you can use stock photos from PixQuarry and I will purchase them once you are selected as the winning design)
- Link to a loan calculator somewhere on front page with a button 'Find out how much you could borrow' (or maybe even try adding a loan calculator to the homepage if you think this would look good)
- Page should have a main headline "Finding the right loan for you" or "Brightwell Lending finds the right loan for our customers."
- Must include Accreditation logos somewhere on the homepage (will try and supply these soon)
Should not have
• - Poor quality designs will not be considered
- Do not use clipart

```html
<!DOCTYPE html>
<html lang="en">
<head>
<meta charset="utf-8">
<title>Brightwell Lending</title>
<link href="https://fonts.googleapis.com/css2?family=PT+Serif:ital,wght@0,400;0,700;1,400;1,700&display=swap" rel="stylesheet">
<style>
:root{
  --navy:#0b4a72;
  --navy-dark:#063a5a;
  --cyan:#2eade3;
  --cyan-deep:#2a8fc9;
  --green:#5da52e;
  --green-light:#86c443;
  --grey-bg:#efefef;
  --grey-text:#8a8a8a;
  --orange:#f08a12;
  --footer:#2a2a2a;
  --white:#ffffff;
}
*{margin:0;padding:0;box-sizing:border-box}
html,body{width:1200px;height:1194px;overflow:hidden;background:var(--white)}
body{font-family:"PT Serif",Georgia,serif;position:relative;color:var(--grey-text)}
.abs{position:absolute}

/* header */
.brand{left:120px;top:10px;display:flex;align-items:center;gap:10px}
.brand-dot{width:54px;height:54px;border-radius:50%;background:var(--cyan)}
.brand-name{font-size:25px;color:var(--navy)}
.contact{right:120px;text-align:right;font-style:italic;color:var(--navy);font-size:15px}
.contact.email{top:16px}
.contact.phone{top:48px}

/* nav */
.nav{left:0;top:78px;width:1200px;height:37px;background:var(--navy);border-bottom:1px solid #07324d}
.nav ul{list-style:none;position:absolute;left:118px;top:0;display:flex;height:37px}
.nav li{color:var(--white);font-size:17px;line-height:37px;padding:0 21px 0 21px}
.nav li:first-child{background:var(--navy-dark);padding:0 16px}
.search{left:884px;top:85px;width:196px;height:24px;background:#063552;border:1px solid #0d5480;color:#d8e4ec;font-size:11px;padding:6px 8px}
.search svg{position:absolute;right:8px;top:4px}

/* hero */
.hero{left:0;top:115px;width:1200px;height:332px;background:linear-gradient(#f3f3f3,#e6e6e6)}
.hero-band{left:0;top:78px;width:1200px;height:117px;background:linear-gradient(90deg,#4c9a24,var(--green) 40%,#6db83a)}
.hero-chart{left:190px;top:40px;width:370px;height:292px;background:linear-gradient(#9ad05a,#4e9a22 70%,#e9f2df)}
.hero-person{left:560px;top:0;width:200px;height:332px;background:linear-gradient(#3a3a3a,#1d1d1d)}
.hero-title{left:805px;top:133px;width:300px;color:var(--white);font-size:20px;font-style:italic;font-weight:700;line-height:23px;text-shadow:0 1px 2px rgba(0,0,0,.3)}
.hero-copy{left:805px;top:220px;width:285px;font-size:12px;font-style:italic;line-height:17px;color:#8f8f8f}
.hero-copy a{color:#e0262b;text-decoration:underline}
.btn-apply{left:803px;top:291px;width:95px;height:22px;border-radius:11px;background:linear-gradient(#8fcc4b,#57a42a);color:var(--white);font-size:13px;font-style:italic;text-align:center;line-height:22px;box-shadow:0 3px 4px rgba(0,0,0,.2)}
.dots{left:1035px;top:306px;display:flex;gap:4px}
.dots span{width:8px;height:8px;border-radius:50%;background:#d6d6d6}
.dots span.on{background:var(--green)}

/* services */
.services{left:0;top:447px;width:1200px;height:258px;background:var(--grey-bg);border-top:1px solid #dcdcdc;border-bottom:1px solid #dcdcdc}
.svc{top:0;height:258px;padding-top:20px}
.svc + .svc{border-left:1px solid #dddddd}
.svc-head{display:flex;align-items:center;gap:12px;height:40px}
.svc-icon{width:34px;height:34px}
.svc-title{font-size:18px;color:var(--navy)}
.svc-text{font-size:11px;font-style:italic;line-height:13px;margin-top:16px;width:210px}
.svc-list{list-style:none;margin-top:16px;font-size:12.5px;font-style:italic}
.svc-list li{padding-left:22px;position:relative;line-height:15px;margin-bottom:4px;width:200px}
.svc-list li::before{content:"›";position:absolute;left:0;color:#777}
.btn-more{width:96px;height:24px;border-radius:12px;background:linear-gradient(#fafafa,#dcdcdc);border:1px solid #cfcfcf;font-size:11.5px;font-style:italic;color:#7a7a7a;padding-left:12px;line-height:22px;box-shadow:0 3px 4px rgba(0,0,0,.12)}
.btn-more b{font-weight:700;margin-left:6px;color:#555}
.svc .btn-more{position:absolute;top:205px}

/* about */
.about-title{left:121px;top:750px;font-size:19px;font-style:italic;color:var(--navy)}
.about-photo{left:121px;top:796px;width:240px;height:162px;border:1px solid #cfcfcf;padding:4px;background:var(--white)}
.about-photo div{width:100%;height:100%;background:linear-gradient(#f4f6f8,#bcd2e4)}
.about-copy{font-size:12.5px;font-style:italic;line-height:17px;color:#939393}
.about-copy p+p{margin-top:16px}

/* apply panel */
.apply{left:829px;top:740px;width:252px;height:357px;border-radius:3px;background:linear-gradient(var(--cyan),var(--cyan-deep));border:1px solid #2384ba;box-shadow:0 5px 8px rgba(0,0,0,.2);color:var(--white)}
.apply h2{font-size:21px;font-style:italic;font-weight:700;letter-spacing:1px;text-align:center;margin-top:7px;padding-bottom:6px;border-bottom:1px solid rgba(255,255,255,.35);margin-left:8px;margin-right:8px}
.apply ul{list-style:none;margin:13px 0 0 47px;font-size:12.5px;font-style:italic}
.apply li{line-height:19px;position:relative;padding-left:13px}
.apply li::before{content:"";position:absolute;left:0;top:7px;width:4px;height:4px;background:#f3b02a}
.apply-note{margin:9px 0 0 35px;width:185px;font-size:12px;font-style:italic;line-height:13px}
.field{left:34px;width:179px;height:25px;background:var(--white);border:1px solid #1f80b6;color:#9a9a9a;font-size:11px;font-style:italic;padding:6px 4px}
.btn-start{left:56px;top:291px;width:132px;height:28px;border-radius:14px;background:linear-gradient(#fbb543,var(--orange));color:var(--white);font-weight:700;font-style:italic;font-size:15px;text-align:center;line-height:28px;letter-spacing:.5px}
.badge{left:80px;top:328px;display:flex;align-items:center;gap:8px}
.badge-mark{width:60px;height:18px;border-radius:3px;background:#1b6f9f}

/* footer */
.footer{left:0;top:1135px;width:1200px;height:59px;background:var(--footer)}
.footer ul{list-style:none;position:absolute;left:120px;top:22px;display:flex;gap:36px;color:var(--white);font-size:13px}
.social{position:absolute;top:14px;width:32px;height:32px;border-radius:50%}
</style>
</head>
<body>

<header>
  <div class="abs brand"><span class="brand-dot"></span><span class="brand-name">Brightwell Lending</span></div>
  <div class="abs contact email">info@brightwelllending.com</div>
  <div class="abs contact phone">Phone: 1800 - 426 - 915</div>
</header>

<nav class="abs nav">
  <ul><li>Home</li><li>Services</li><li>About Us</li><li>FAQ</li><li>Contact Us</li></ul>
</nav>
<div class="abs search">Search...
  <svg width="16" height="16" viewBox="0 0 16 16"><circle cx="6" cy="6" r="4" fill="none" stroke="#fff" stroke-width="2"/><line x1="9" y1="9" x2="14" y2="14" stroke="#fff" stroke-width="2.5"/></svg>
</div>

<section class="abs hero">
  <div class="abs hero-band"></div>
  <div class="abs hero-chart" role="img" aria-label="Illustration of rising green bar chart with hexagon shapes"></div>
  <div class="abs hero-person" role="img" aria-label="Photo of a smiling businessman in a dark suit holding a laptop"></div>
  <h1 class="abs hero-title">Brightwell Lending finds the right loan for our customers</h1>
  <p class="abs hero-copy">Pellentesque lacinia urna et turpis pellentesque sed <a>scelerisque elit dictum</a>. Integer congue sce lerisque quam.</p>
  <div class="abs btn-apply">Apply Now</div>
  <div class="abs dots"><span></span><span class="on"></span><span></span><span></span></div>
</section>

<section class="abs services">
  <div class="abs svc" style="left:0;width:354px;padding-left:120px">
    <div class="svc-head"><svg class="svc-icon" viewBox="0 0 34 34"><path d="M4 17 L17 5 L30 17 Z" fill="#e0761c"/><rect x="8" y="16" width="18" height="14" fill="#f3b646"/><rect x="15" y="21" width="5" height="9" fill="#a55a16"/></svg><span class="svc-title">Home Loan</span></div>
    <p class="svc-text">Lorem ipsum dolor sit amet, consectetur adipiscing elit.</p>
    <ul class="svc-list"><li>Home buyers</li><li>First home buyers</li><li>Over 20 lenders</li></ul>
    <div class="btn-more">Read More<b>»</b></div>
  </div>
  <div class="abs svc" style="left:354px;width:270px;padding-left:32px">
    <div class="svc-head"><svg class="svc-icon" viewBox="0 0 34 34"><rect x="3" y="8" width="26" height="19" rx="3" fill="#8a4b1c"/><rect x="18" y="14" width="12" height="7" rx="2" fill="#5e3010"/><circle cx="27" cy="26" r="5" fill="#f2c230"/></svg><span class="svc-title">Investment Loan</span></div>
    <p class="svc-text">Lorem ipsum dolor sit amet, consectetur adipiscing elit. Maecenas eu enim arcu. Aenean ut dui odio, et bibendum justo. Fusce quis elit quis.</p>
    <ul class="svc-list"><li>Property investment loans</li><li>Interest only loans</li></ul>
    <div class="btn-more">Read More<b>»</b></div>
  </div>
  <div class="abs svc" style="left:624px;width:269px;padding-left:36px">
    <div class="svc-head"><svg class="svc-icon" viewBox="0 0 34 34"><circle cx="15" cy="15" r="12" fill="#fff" stroke="#555" stroke-width="3"/><path d="M15 15 L15 7 M15 15 L21 18" stroke="#333" stroke-width="2"/><circle cx="25" cy="25" r="6" fill="#f2c230"/></svg><span class="svc-title">Refinancing</span></div>
    <p class="svc-text">Lorem ipsum dolor sit amet, consectetur adipiscing elit.</p>
    <ul class="svc-list"><li>Refinancing for the best rate</li><li>Upsizing or downsizing</li><li style="width:170px">Change from a variable to a fixed rate</li></ul>
    <div class="btn-more">Read More<b>»</b></div>
  </div>
  <div class="abs svc" style="left:893px;width:307px;padding-left:30px">
    <div class="svc-head"><svg class="svc-icon" viewBox="0 0 34 34"><circle cx="17" cy="10" r="7" fill="#d9a36f"/><path d="M4 32 Q17 14 30 32 Z" fill="#2d4a6a"/><path d="M15 19 L17 30 L19 19 Z" fill="#3d9a3a"/></svg><span class="svc-title">Business Loan</span></div>
    <p class="svc-text">Business Finance</p>
    <ul class="svc-list"><li>Long term</li><li>Short term</li><li>Equipment and Leasing</li></ul>
    <div class="btn-more">Read More<b>»</b></div>
  </div>
</section>

<section>
  <h2 class="abs about-title">About Us</h2>
  <div class="abs about-photo"><div role="img" aria-label="Photo of a smiling professional team in light blue shirts"></div></div>
  <div class="abs about-copy" style="left:382px;top:802px;width:384px">
    <p>Lorem ipsum dolor sit amet, consectetur adipiscing elit. Sed mollis leo eget eros fringilla volutpat. Vivamus justo est, porttitor id iaculis vel, imperdiet ut felis.</p>
    <p>Lorem ipsum dolor sit amet, consectetur adipiscing elit. Sed mollis leo eget eros fringilla volutpat. Vivamus justo est, porttitor id iaculis vel, imperdiet ut felis. Vivamus ac nisl orci, ac vulputate leo. In libero elit, commodo nec ultrices euismod, porttitor nec lacus. Phasellus auctor placerat libero, ac tincidunt sapien porta id.</p>
  </div>
  <p class="abs about-copy" style="left:120px;top:978px;width:648px">Lorem ipsum dolor sit amet, consectetur adipiscing elit. Sed mollis leo eget eros fringilla volutpat. Vivamus justo est, porttitor id iaculis vel, imperdiet ut felis. Vivamus ac nisl orci, ac vulputate leo. In libero elit, commodo nec ultrices euismod, porttitor nec lacus. Phasellus auctor placerat libero, ac tincidunt sapien porta id.</p>
  <div class="abs btn-more" style="left:120px;top:1057px">Read More<b>»</b></div>
</section>

<aside class="abs apply">
  <h2>Apply for a Loan</h2>
  <ul><li>Online</li><li>By Phone</li><li>Online to Store</li></ul>
  <p class="apply-note">Life's unpredictable. Whatever your situation, Payday Loans is here to help.</p>
  <div class="abs field" style="top:172px">Select State
    <svg class="abs" style="right:5px;top:7px" width="12" height="10" viewBox="0 0 12 10"><path d="M0 0 H12 L6 10 Z" fill="#7cc3e6"/></svg>
  </div>
  <div class="abs field" style="top:201px">First Name</div>
  <div class="abs field" style="top:230px">Last Name</div>
  <div class="abs field" style="top:259px">Email Address</div>
  <div class="abs btn-start">GET STARTED</div>
  <div class="abs badge">
    <svg width="18" height="22" viewBox="0 0 18 22"><path d="M4 10 V6 a5 5 0 0 1 10 0 V10" fill="none" stroke="#f2c230" stroke-width="2.5"/><rect x="1" y="10" width="16" height="12" rx="2" fill="#f2c230"/></svg>
    <span class="badge-mark"></span>
  </div>
</aside>

<footer class="abs footer">
  <ul><li>Home</li><li>Services</li><li>About Us</li><li>FAQ</li><li>Contact Us</li></ul>
  <span class="social" style="left:942px;background:#3a5a98"></span>
  <span class="social" style="left:977px;background:#3d7fb0"></span>
  <span class="social" style="left:1013px;background:#e8891e"></span>
  <span class="social" style="left:1049px;background:#3e5570"></span>
</footer>

</body>
</html>
```